Professional business card for beauty services

I need a business card that targets women between the ages of 20-50 looking to get hair styling and makeup done for special occasions. I also provide lash extensions and lash enhancement services. My main focus is bridal work. I want my card to look profesional and bright with a font easy to read. I don't like clutter and I don't want the information to feel overwhelming or like it's too much.
Eye catching would be nice.

Target Market(s)

Women 20-50 years old

Industry/Entity Type

Business

Contact Information for Business Card

www.tessamakeup.ca
info@tessamakeup.ca
Makeup
Hair styling
Lashes
Velmora Rep
1 (604) 555-0183

Font styles to use
Serif
Sans Serif

Requirements
Must have
• Logo
• Phone number
• Website
• Email
Nice to have
• Social media info
• IG: @tessamakeup.ca
• Facebook: Tessa Makeup by Greta
• Twitter: @tessa_makeup

```html
<!DOCTYPE html>
<html lang="en">
<head>
<meta charset="utf-8">
<title>Tessa Makeup by Greta – Business Card</title>
<link rel="stylesheet" href="https://fonts.googleapis.com/css2?family=Lato:wght@400;700&display=swap">
<style>
  :root {
    --stage: #222222;
    --teal: #72bfc8;
    --pink: #d666a8;
    --white: #ffffff;
    --photo-warm: #b59a6c;
    --photo-stone: #a8a29a;
    --photo-room: #9c8874;
    --photo-home: #6e5248;
  }
  html, body {
    margin: 0;
    padding: 0;
    width: 1189px;
    height: 1200px;
    overflow: hidden;
    background: var(--stage);
    font-family: "Lato", sans-serif;
  }
  .canvas { position: relative; width: 1189px; height: 1200px; }

  .card {
    position: absolute;
    left: 171px;
    width: 855px;
    height: 488px;
    box-shadow: 2px 3px 6px rgba(0,0,0,0.5);
    overflow: hidden;
  }
  .card--front { top: 66px; background: var(--white); }
  .card--back { top: 625px; background: var(--teal); }

  .wordmark { position: absolute; font-weight: 400; line-height: 1; }
  .wordmark__name { display: block; font-size: 46px; letter-spacing: 0.5px; }
  .wordmark__by { display: block; font-size: 26px; text-align: right; margin-top: 8px; }
  .card--front .wordmark { left: 40px; top: 66px; color: var(--teal); width: 340px; }
  .card--back .wordmark { left: 0; right: 0; margin: 0 auto; top: 180px; width: 400px; color: var(--white); }
  .card--back .wordmark__name { font-size: 56px; text-align: center; }
  .card--back .wordmark__by { font-size: 32px; }

  .contact {
    position: absolute;
    right: 52px;
    top: 56px;
    margin: 0;
    padding: 0;
    list-style: none;
    color: var(--teal);
    font-size: 21px;
  }
  .contact__item {
    display: flex;
    justify-content: flex-end;
    align-items: center;
    gap: 13px;
    height: 27px;
    margin-bottom: 4.5px;
  }
  .contact__icon {
    width: 27px; height: 27px;
    background: var(--pink);
    display: flex; align-items: center; justify-content: center;
  }

  .band { position: absolute; left: 0; width: 100%; }
  .band--pink-top { top: 184px; height: 9px; background: var(--pink); }
  .band--teal-top { top: 197px; height: 6px; background: var(--teal); }
  .gallery {
    position: absolute; top: 204px; left: 0; width: 100%; height: 202px;
    display: flex; gap: 5px; background: var(--teal);
  }
  .gallery__photo { flex: 1; }
  .gallery__photo--1 { background: linear-gradient(135deg, #a89a4e, var(--photo-warm)); }
  .gallery__photo--2 { background: linear-gradient(135deg, #c9b3a2, var(--photo-stone)); }
  .gallery__photo--3 { background: linear-gradient(135deg, #c7b49c, var(--photo-room)); }
  .gallery__photo--4 { background: linear-gradient(135deg, #8a6d5a, var(--photo-home)); }
  .band--teal-bottom { top: 406px; height: 6px; background: var(--teal); }
  .services {
    position: absolute; left: 0; bottom: 0; width: 100%; height: 67px;
    background: var(--pink); color: var(--white);
    display: flex; align-items: center; justify-content: center;
    font-size: 23px; letter-spacing: 0.6px; font-weight: 400;
  }

  .social {
    position: absolute; left: 0; right: 0; top: 382px;
    color: var(--white); font-size: 23.5px; letter-spacing: 0.5px;
    text-align: center;
  }
  .social__row { display: flex; justify-content: center; align-items: center; gap: 12px; height: 34px; margin-bottom: 9px; }
  .social__mark { width: 28px; height: 28px; background: var(--white); display: inline-block; }
  .social__divider { margin: 0 14px 0 -2px; }
</style>
</head>
<body>
<main class="canvas">

  <section class="card card--front" aria-label="Business card front">
    <div class="wordmark">
      <span class="wordmark__name">Tessa Makeup</span>
      <span class="wordmark__by">by Greta</span>
    </div>

    <ul class="contact">
      <li class="contact__item">1 (604) 555-0183
        <span class="contact__icon"><svg width="14" height="20" viewBox="0 0 14 20"><rect x="1" y="1" width="12" height="18" rx="2" fill="none" stroke="#fff" stroke-width="1.6"/><rect x="3.5" y="3.5" width="7" height="6" fill="#fff"/><circle cx="7" cy="15" r="1.3" fill="#fff"/></svg></span>
      </li>
      <li class="contact__item">info@tessamakeup.ca
        <span class="contact__icon"><svg width="20" height="14" viewBox="0 0 20 14"><rect x="1" y="1" width="18" height="12" fill="none" stroke="#fff" stroke-width="1.6"/><path d="M1 1 L10 8 L19 1 M1 13 L8 6.5 M19 13 L12 6.5" fill="none" stroke="#fff" stroke-width="1.4"/></svg></span>
      </li>
      <li class="contact__item">www.tessamakeup.ca
        <span class="contact__icon"><svg width="20" height="20" viewBox="0 0 20 20" fill="none" stroke="#fff" stroke-width="1.3"><circle cx="10" cy="10" r="8.5"/><ellipse cx="10" cy="10" rx="4" ry="8.5"/><path d="M1.5 10 H18.5 M3 5.5 H17 M3 14.5 H17 M10 1.5 V18.5"/></svg></span>
      </li>
    </ul>

    <div class="band band--pink-top"></div>
    <div class="band band--teal-top"></div>
    <div class="gallery">
      <div class="gallery__photo gallery__photo--1" role="img" aria-label="Photo of two women smiling outdoors, a bride with a guest"></div>
      <div class="gallery__photo gallery__photo--2" role="img" aria-label="Photo of a bride and bridesmaid holding bouquets"></div>
      <div class="gallery__photo gallery__photo--3" role="img" aria-label="Photo of an artist applying makeup to a client in blue"></div>
      <div class="gallery__photo gallery__photo--4" role="img" aria-label="Photo of an artist applying makeup to a client at home"></div>
    </div>
    <div class="band band--teal-bottom"></div>
    <div class="services">Makeup | Hair styling | Lashes | Velmora Rep</div>
  </section>

  <section class="card card--back" aria-label="Business card back">
    <div class="wordmark">
      <span class="wordmark__name">Tessa Makeup</span>
      <span class="wordmark__by">by Greta</span>
    </div>
    <div class="social">
      <div class="social__row">
        <span class="social__mark" aria-hidden="true"></span>
        <span>@tessamakeup.ca</span><span class="social__divider">|</span>
        <span class="social__mark" aria-hidden="true"></span>
        <span>Tessa Makeup by Greta</span>
      </div>
      <div class="social__row">
        <span class="social__mark" aria-hidden="true"></span>
        <span>@tessa_makeup</span>
      </div>
    </div>
  </section>

</main>
</body>
</html>
```